slide deck template design needed for sales and presales presentations

We would like to have a bright and light, contemporary slide deck design based on our existing style assets (see attached files).
We are based in Latvia. Our business is ERP systems implementation, IT infrastructure building and supporting our customers. We are moving from traditional Add-hoc projects model to standardized flat-rate offerings. Our technology platform is Quintavel.
The value proposition of our offerings is based around simplicity, transparency, quality, peace of mind, trust, easy of doing business.
I have to add that if any special are being used, they must be unicode to ensure proper Latvian language characters display.
Updates
Hi! The reason is an error at your side. Today it's 24/08/2020 when I started the project and made a payment. Still for some funny reason in the BRIEF I see that the project deadline is set to 20/08/2020. No wonder no designers are applying...
Target Market(s)
Small and medium enterprise
Look and feel

```html
<!DOCTYPE html>
<html lang="en">
<head>
<meta charset="utf-8">
<title>Meadowline – Presentation Template</title>
<link rel="stylesheet" href="https://fonts.googleapis.com/css2?family=Montserrat:wght@400;500;600;700;800&family=Open+Sans:wght@400;600&display=swap">
<style>
:root{
  --ink:#0e0e0e;
  --teal:#13b5b1;
  --green:#8dc63f;
  --yellow:#fcc71a;
  --grey:#8a8a8a;
  --light:#f3f3f3;
  --canvas:#ffffff;
  --line:#d9d9d9;
}
*{box-sizing:border-box;margin:0;padding:0}
html,body{width:1200px;height:3726px;overflow:hidden;background:var(--canvas)}
body{font-family:"Montserrat",sans-serif;color:var(--ink)}
.deck{display:grid;grid-template-columns:551px 551px;grid-auto-rows:309px;column-gap:23px;row-gap:26px;padding:32px 0 0 36px}
.slide{position:relative;width:551px;height:309px;background:#fff;overflow:hidden;box-shadow:0 2px 8px rgba(0,0,0,.18)}
.slide.dark{background:var(--ink);color:#fff}
.abs{position:absolute}
.title{font-weight:800;font-size:19px;letter-spacing:.2px;line-height:1.1}
.sub{font-size:5.5px;letter-spacing:3px;color:var(--grey);margin-top:5px;font-weight:500}
.body{font-family:"Open Sans",sans-serif;font-size:5.6px;line-height:1.45;color:#555}
.dark .body{color:#ddd}
.wordmark{position:absolute;font-weight:700;letter-spacing:.12em;white-space:nowrap}
.foot{position:absolute;left:10px;bottom:8px;font-size:4px;color:#666;letter-spacing:.3px}
.page{position:absolute;right:14px;bottom:8px;font-size:4px;color:#666}
.stripe{position:absolute;left:0;right:0;bottom:0;height:4px;display:flex}
.stripe i{display:block;height:100%}
.stripe .k{flex:1;background:var(--ink)}
.stripe .t{width:50px;background:var(--teal)}
.stripe .g{width:50px;background:var(--green)}
.stripe .y{width:50px;background:var(--yellow)}
.photo{position:absolute}
.bg-teal{background:var(--teal)}.bg-green{background:var(--green)}.bg-yellow{background:var(--yellow)}.bg-ink{background:var(--ink)}
.list li{list-style:none;margin-bottom:3px}
.bullet li::before{content:"✓ ";color:var(--ink)}
.dark-list li::before{color:#fff}
.agenda-item{display:flex;align-items:center;gap:10px;font-weight:700;font-size:7px;margin-bottom:24px}
.agenda-item b{display:flex;width:14px;height:14px;border-radius:50%;background:var(--ink);color:#fff;align-items:center;justify-content:center;font-size:7px}
table.grid{border-collapse:collapse;font-size:5.5px;font-family:"Open Sans",sans-serif}
.price-col{position:absolute;top:84px;width:86px;text-align:center}
.price-col .head{background:var(--ink);color:#fff;font-size:5px;font-weight:700;padding:4px 0}
.price-col .amt{color:#fff;font-size:17px;font-weight:700;padding:4px 0 1px}
.price-col .opt{font-size:4.5px;color:#666;border-bottom:1px solid var(--line);padding:4px 0}
.price-col .foot-btn{background:var(--ink);color:#fff;font-size:5px;font-weight:700;padding:4px 0;margin-top:4px}
.partner{position:absolute;width:82px;height:26px;display:flex;align-items:center;justify-content:center;gap:4px;font-weight:600;font-size:9px;color:#555;background:#fff;box-shadow:0 1px 3px rgba(0,0,0,.12)}
.partner .sq{width:8px;height:8px;background:var(--teal)}
.member{position:absolute;top:74px;width:104px;text-align:center}
.member .pic{height:110px;background:linear-gradient(#7a6a5c,#c9b8a6)}
.member .name{color:#fff;font-size:6px;font-weight:600;padding:3px 0}
.step{position:absolute;width:58px;height:32px;background:#fff;box-shadow:0 1px 4px rgba(0,0,0,.2);border-radius:3px;display:flex;align-items:center;justify-content:center;font-size:8px;font-weight:500}
.node{position:absolute;width:28px;height:28px;border:1.2px solid var(--ink);background:#fff}
</style>
</head>
<body>
<main class="deck">

<section class="slide">
  <div class="wordmark" style="left:100px;top:128px;font-size:24px">MEADOWLINE</div>
  <div class="abs" style="right:22px;top:80px;writing-mode:vertical-rl;transform:rotate(180deg);font-size:6px;letter-spacing:2px">WWW.MEADOWLINE-STUDIO.COM</div>
</section>

<section class="slide">
  <div class="photo" role="img" aria-label="Light grey connected network of dots and lines" style="left:290px;top:0;width:261px;height:300px;background:linear-gradient(135deg,#fff,#ececec)"></div>
  <div class="wordmark" style="left:52px;top:106px;font-size:16px">MEADOWLINE</div>
  <div class="abs" style="left:52px;top:222px;font-size:5px;letter-spacing:3px;font-weight:600">WWW.MEADOWLINE-STUDIO.COM</div>
  <div class="abs bg-ink" style="left:0;bottom:0;width:375px;height:10px"><span style="color:#fff;font-size:4px;position:absolute;left:16px;top:3px">MEADOWLINE | CLEAR IT FOR GROWTH</span></div>
  <div class="abs bg-teal" style="left:383px;bottom:0;width:52px;height:10px"></div>
  <div class="abs bg-green" style="left:441px;bottom:0;width:52px;height:10px"></div>
  <div class="abs bg-yellow" style="left:499px;bottom:0;width:52px;height:10px"></div>
</section>

<section class="slide">
  <div class="photo" role="img" aria-label="Grey toned photo of hands working on a laptop" style="inset:0;background:linear-gradient(90deg,#f4f4f4 30%,#bdbdbd 70%,#8d8d8d)"></div>
  <div class="abs" style="left:14px;top:14px;width:520px;height:284px;border:2px solid var(--ink);border-right-color:var(--yellow);border-bottom-color:var(--teal)"></div>
  <div class="wordmark" style="left:54px;top:50px;font-size:14px">MEADOWLINE</div>
  <div class="abs" style="left:52px;top:150px;font-size:8px">2020</div>
  <div class="abs title" style="left:52px;top:164px">MASTER SLIDE<br>TEMPLATE</div>
  <div class="abs sub" style="left:52px;top:212px">SUBTITLE GOES HERE</div>
  <div class="abs" style="left:52px;top:236px;display:flex;gap:3px"><i style="width:9px;height:9px;border-radius:50%;border:1px solid #222;display:block"></i><i style="width:9px;height:9px;border-radius:50%;border:1px solid #222;display:block"></i><i style="width:9px;height:9px;border-radius:50%;border:1px solid #222;display:block"></i><i style="width:9px;height:9px;border-radius:50%;border:1px solid #222;display:block"></i></div>
</section>

<section class="slide dark">
  <div class="abs bg-teal" style="left:376px;top:0;width:56px;height:309px"></div>
  <div class="abs bg-green" style="left:434px;top:0;width:56px;height:309px"></div>
  <div class="abs bg-yellow" style="left:492px;top:0;width:59px;height:309px"></div>
  <div class="wordmark" style="left:52px;top:62px;font-size:14px">MEADOWLINE</div>
  <div class="abs title" style="left:52px;top:170px">MASTER SLIDE<br>TEMPLATE</div>
  <div class="abs sub" style="left:52px;top:216px;color:#bbb">SUBTITLE GOES HERE</div>
  <div class="abs" style="left:52px;top:265px;display:flex;gap:3px"><i style="width:9px;height:9px;border-radius:50%;border:1px solid #fff;display:block"></i><i style="width:9px;height:9px;border-radius:50%;border:1px solid #fff;display:block"></i><i style="width:9px;height:9px;border-radius:50%;border:1px solid #fff;display:block"></i><i style="width:9px;height:9px;border-radius:50%;border:1px solid #fff;display:block"></i></div>
  <div class="abs" style="left:326px;top:270px;font-size:8px">2020</div>
</section>

<section class="slide">
  <div class="photo" role="img" aria-label="Business person with glowing ERP network graphic over a city" style="left:0;top:0;width:551px;height:230px;background:linear-gradient(90deg,#c9745b,#6b7887 45%,#aeb6c0)"></div>
  <div class="abs" style="left:66px;top:90px;color:#fff;font-weight:800;font-size:38px">ERP</div>
  <div class="abs" style="left:62px;top:134px;color:#fff;font-size:6px;text-align:center;width:90px">ENTERPRISE RESOURCE PLANNING</div>
  <div class="wordmark" style="left:440px;top:22px;font-size:7px;color:#fff">MEADOWLINE</div>
  <div class="abs title" style="left:24px;top:258px;font-size:18px">What is ERP?</div>
  <div class="abs" style="left:214px;top:248px;width:1px;height:42px;background:var(--ink)"></div>
  <div class="abs body" style="left:232px;top:250px;width:300px">Lorem ipsum dolor sit amet, consectetuer adipiscing elit, sed diam nonummy nibh euismod tincidunt ut laoreet dolore magna aliquam erat volutpat. Ut wisi enim ad minim veniam, quis nostrud exerci tation ullamcorper suscipit lobortis nisl ut aliquip ex ea commodo consequat.</div>
</section>

<section class="slide">
  <div class="abs bg-ink" style="left:0;top:0;width:142px;height:309px"></div>
  <div class="abs" style="left:22px;top:20px;color:#fff;font-size:5px;font-weight:700">TEXT HERE</div>
  <div class="abs" style="left:22px;top:132px;width:30px;height:2px;background:linear-gradient(90deg,var(--teal),var(--green),var(--yellow))"></div>
  <div class="abs" style="left:22px;top:142px;color:#fff;font-weight:800;font-size:19px">AGENDA</div>
  <div class="wordmark" style="left:22px;top:274px;font-size:5px;color:#fff">MEADOWLINE</div>
  <div class="photo" role="img" aria-label="Busy city street crowd in muted grey tones" style="left:142px;top:0;width:168px;height:309px;background:linear-gradient(#b7b9bd,#6b6c70)"></div>
  <div class="abs" style="left:314px;top:34px">
    <div class="agenda-item"><b>›</b>INTRODUCTION</div>
    <div class="agenda-item"><b>›</b>ABOUT US</div>
    <div class="agenda-item"><b>›</b>WELCOME MASSAGE</div>
    <div class="agenda-item"><b>›</b>OUR SERVICES</div>
    <div class="agenda-item"><b>›</b>OUR TEAM</div>
    <div class="agenda-item"><b>›</b>CONTACT US</div>
  </div>
  <div class="abs bg-teal" style="right:0;top:0;width:4px;height:309px"></div>
</section>

<section class="slide">
  <div class="photo" role="img" aria-label="Smiling businessman reading a yellow notebook at a desk" style="left:310px;top:0;width:241px;height:309px;background:linear-gradient(90deg,#d8d3cb,#8e8a85)"></div>
  <div class="abs" style="left:14px;top:14px;width:300px;height:284px;border:2px solid var(--ink);background:#fff"></div>
  <div class="wordmark" style="left:338px;top:42px;font-size:6px">MEADOWLINE</div>
  <div class="abs title" style="left:98px;top:52px;text-align:right;width:184px;font-size:18px">YOUR TITLE HERE</div>
  <div class="abs sub" style="left:98px;top:74px;text-align:right;width:184px">SUBTITLE GOES HERE</div>
  <div class="abs body" style="left:40px;top:100px;width:250px;text-align:center">Lorem ipsum dolor sit amet, consectetuer adipiscing elit, sed diam nonummy nibh euismod tincidunt ut laoreet dolore magna aliquam erat volutpat. Ut wisi enim ad minim veniam, quis nostrud exerci tation ullamcorper suscipit lobortis nisl ut aliquip ex ea commodo consequat</div>
  <div class="abs bg-teal" style="left:64px;top:214px;width:30px;height:30px"></div>
  <div class="abs bg-green" style="left:146px;top:214px;width:30px;height:30px"></div>
  <div class="abs bg-yellow" style="left:228px;top:214px;width:30px;height:30px"></div>
  <div class="abs" style="left:50px;top:264px;font-size:6px;width:240px;display:flex;justify-content:space-between"><span>Content Here</span><span>Content Here</span><span>Content Here</span></div>
</section>

<section class="slide">
  <div class="abs title" style="left:32px;top:22px">YOUR TITLE HERE</div>
  <div class="abs sub" style="left:32px;top:44px">SUBTITLE GOES HERE</div>
  <div class="wordmark" style="left:438px;top:30px;font-size:6px">MEADOWLINE</div>
  <div class="photo" role="img" aria-label="Smiling colleagues collaborating in an office" style="left:14px;top:74px;width:524px;height:84px;background:linear-gradient(90deg,#bfb8ae,#e6e2dc 50%,#b8b1a9)"></div>
  <div class="abs bg-teal" style="left:76px;top:138px;width:36px;height:36px;border-radius:50%;border:3px solid #fff"></div>
  <div class="abs bg-green" style="left:256px;top:138px;width:36px;height:36px;border-radius:50%;border:3px solid #fff"></div>
  <div class="abs bg-yellow" style="left:436px;top:138px;width:36px;height:36px;border-radius:50%;border:3px solid #fff"></div>
  <ul class="abs body list bullet" style="left:44px;top:198px;width:150px"><li>Lorem ipsum dolor sit amet,</li><li>consectetuer adipiscing elit,</li><li>sed diam nonummy nibh</li><li>euismod tincidunt ut laoreet</li><li>dolore magna aliquam erat</li></ul>
  <ul class="abs body list bullet" style="left:224px;top:198px;width:150px"><li>Lorem ipsum dolor sit amet,</li><li>consectetuer adipiscing elit,</li><li>sed diam nonummy nibh</li><li>euismod tincidunt ut laoreet</li><li>dolore magna aliquam erat</li></ul>
  <ul class="abs body list bullet" style="left:404px;top:198px;width:140px"><li>Lorem ipsum dolor sit amet,</li><li>consectetuer adipiscing elit,</li><li>sed diam nonummy nibh</li><li>euismod tincidunt ut laoreet</li><li>dolore magna aliquam erat</li></ul>
  <div class="foot">MEADOWLINE | CLEAR IT FOR GROWTH</div><div class="page">PAGE | 8</div>
  <div class="stripe"><i class="k"></i><i class="t"></i><i class="g"></i><i class="y"></i></div>
</section>

<section class="slide">
  <div class="abs title" style="left:32px;top:22px">YOUR TITLE HERE</div>
  <div class="abs sub" style="left:32px;top:44px">SUBTITLE GOES HERE</div>
  <div class="wordmark" style="left:438px;top:30px;font-size:6px">MEADOWLINE</div>
  <div class="abs" style="left:66px;top:104px;width:196px;height:124px;border:6px solid var(--ink);border-radius:4px;background:#fff"></div>
  <div class="abs" style="left:48px;top:228px;width:232px;height:6px;background:#ccc;border-radius:0 0 6px 6px"></div>
  <div class="abs title" style="left:94px;top:144px;font-size:22px">ERP<br>SYSTEM</div>
  <svg class="abs" style="left:300px;top:70px" width="60" height="200" viewBox="0 0 60 200"><path d="M10 0 Q70 100 10 200" fill="none" stroke="#999" stroke-width="1"/></svg>
  <div class="abs bg-teal" style="left:314px;top:94px;width:26px;height:26px;border-radius:50%"></div>
  <div class="abs bg-green" style="left:322px;top:156px;width:26px;height:26px;border-radius:50%"></div>
  <div class="abs bg-yellow" style="left:310px;top:216px;width:26px;height:26px;border-radius:50%"></div>
  <div class="abs" style="left:362px;top:90px;width:170px"><b style="font-size:8px">Sales</b><p class="body">Get a modern business presentation that is beautifully designed. Easy to change colors, photos and Text.</p></div>
  <div class="abs" style="left:370px;top:150px;width:165px"><b style="font-size:8px">Finance</b><p class="body">Get a modern business presentation that is beautifully designed. Easy to change colors, photos and Text.</p></div>
  <div class="abs" style="left:362px;top:210px;width:170px"><b style="font-size:8px">Supply Chain</b><p class="body">Get a modern business presentation that is beautifully designed. Easy to change colors, photos and Text.</p></div>
  <div class="foot">MEADOWLINE | CLEAR IT FOR GROWTH</div><div class="page">PAGE | 9</div>
  <div class="stripe"><i class="k"></i><i class="t"></i><i class="g"></i><i class="y"></i></div>
</section>

<section class="slide">
  <div class="abs bg-ink" style="left:0;top:0;width:551px;height:52px"></div>
  <div class="abs title" style="left:32px;top:14px;color:#fff">YOUR TITLE HERE</div>
  <div class="abs sub" style="left:32px;top:36px;color:#bbb">SUBTITLE GOES HERE</div>
  <div class="wordmark" style="left:438px;top:22px;font-size:6px;color:#fff">MEADOWLINE</div>
  <div class="abs bg-ink" style="left:78px;top:108px;width:20px;height:134px;border-radius:3px"></div>
  <div class="abs bg-teal" style="left:130px;top:96px;width:118px;height:12px;color:#fff;font-size:5px;text-align:center;line-height:12px;font-weight:600">TEXT HERE</div>
  <div class="abs bg-green" style="left:250px;top:96px;width:118px;height:12px;color:#fff;font-size:5px;text-align:center;line-height:12px;font-weight:600">TEXT HERE</div>
  <div class="abs bg-yellow" style="left:370px;top:96px;width:118px;height:12px;color:#fff;font-size:5px;text-align:center;line-height:12px;font-weight:600">TEXT HERE</div>
  <table class="abs grid" style="left:130px;top:110px;width:358px">
    <tr style="height:26px;border-bottom:1px solid var(--line)"><td align="center">Add Contents Title</td><td align="center">Add Contents Title</td><td align="center">Add Contents Title</td></tr>
    <tr style="height:26px;border-bottom:1px solid var(--line)"><td align="center">Modern Slide Deck</td><td align="center">Modern Slide Deck</td><td align="center">Modern Slide Deck</td></tr>
    <tr style="height:26px;border-bottom:1px solid var(--line)"><td align="center">Add Contents Title</td><td align="center">Add Contents Title</td><td align="center">Add Contents Title</td></tr>
    <tr style="height:26px;border-bottom:1px solid var(--line)"><td align="center">Modern Slide Deck</td><td align="center">Modern Slide Deck</td><td align="center">Modern Slide Deck</td></tr>
    <tr style="height:26px"><td align="center">Add Contents Title</td><td align="center">Add Contents Title</td><td align="center">Add Contents Title</td></tr>
  </table>
  <div class="foot">MEADOWLINE | CLEAR IT FOR GROWTH</div><div class="page">PAGE | 10</div>
  <div class="stripe"><i class="k"></i><i class="t"></i><i class="g"></i><i class="y"></i></div>
</section>

<section class="slide">
  <div class="abs title" style="left:180px;top:20px">YOUR TITLE HERE</div>
  <div class="abs sub" style="left:212px;top:42px">SUBTITLE GOES HERE</div>
  <div class="abs bg-ink" style="left:530px;top:10px;width:14px;height:14px"></div>
  <div class="abs bg-ink" style="left:275px;top:70px;width:276px;height:239px"></div>
  <svg class="abs" style="left:0;top:60px" width="275" height="249" viewBox="0 0 275 249"><g stroke="#999" stroke-dasharray="3 2" fill="none"><line x1="54" y1="20" x2="132" y2="100"/><line x1="136" y1="20" x2="136" y2="100"/><line x1="212" y1="20" x2="140" y2="100"/><line x1="54" y1="100" x2="110" y2="100"/><line x1="212" y1="100" x2="160" y2="100"/><line x1="54" y1="180" x2="132" y2="120"/><line x1="136" y1="180" x2="136" y2="120"/><line x1="212" y1="180" x2="140" y2="120"/></g></svg>
  <div class="node" style="left:40px;top:66px;border-color:var(--teal)"></div>
  <div class="node" style="left:122px;top:66px"></div>
  <div class="node" style="left:198px;top:66px"></div>
  <div class="node" style="left:40px;top:146px;border-color:var(--green)"></div>
  <div class="node" style="left:198px;top:146px"></div>
  <div class="node" style="left:40px;top:226px;border-color:var(--yellow)"></div>
  <div class="node" style="left:122px;top:226px"></div>
  <div class="node" style="left:198px;top:226px"></div>
  <div class="abs" style="left:104px;top:140px;width:64px;height:40px;border:3px solid var(--ink);background:#fff;font-weight:800;font-size:12px;display:flex;align-items:center;justify-content:center">ERP</div>
  <div class="abs" style="left:290px;top:80px;width:250px">
    <p style="color:var(--yellow);font-size:6px;font-weight:600">Content Here</p><p class="body" style="margin-bottom:14px">You can simply impress your audience and add a unique zing and appeal to your Presentations. Easy to change colors, photos and Text.</p>
    <p style="color:var(--yellow);font-size:6px;font-weight:600">Content Here</p><p class="body" style="margin-bottom:14px">You can simply impress your audience and add a unique zing and appeal to your Presentations. Easy to change colors, photos and Text.</p>
    <p style="color:var(--yellow);font-size:6px;font-weight:600">Content Here</p><p class="body" style="margin-bottom:14px">You can simply impress your audience and add a unique zing and appeal to your Presentations. Easy to change colors, photos and Text.</p>
    <p style="color:var(--yellow);font-size:6px;font-weight:600">Content Here</p><p class="body">You can simply impress your audience and add a unique zing and appeal to your Presentations. Easy to change colors, photos and Text.</p>
  </div>
</section>

<section class="slide">
  <div class="wordmark" style="left:232px;top:26px;font-size:6px">MEADOWLINE</div>
  <div class="abs title" style="left:42px;top:76px;font-size:15px">YOUR TITLE HERE</div>
  <div class="abs sub" style="left:42px;top:92px">SUBTITLE GOES HERE</div>
  <div class="abs body" style="left:42px;top:112px;width:136px;text-align:justify">Get a modern business presentation that is beautifully designed. Easy to change colors, photos and Text. You can simply impress your audience and add a unique zing and appeal to your Presentations. Get a modern business presentation that is beautifully designed. Easy to change colors, photos and Text. You can simply impress your audience and add a unique zing and appeal to your Presentations.<br><br>You can simply impress your audience and add a unique zing and appeal to your Presentations.</div>
  <div class="abs bg-ink" style="left:205px;top:72px;width:144px;height:204px;border-radius:8px"></div>
  <ul class="abs body list bullet dark-list" style="left:215px;top:84px;width:126px"><li style="color:#eee;margin-bottom:8px">Get a modern business presentation that is beautifully designed. Easy to change colors, photos and Text.</li><li style="color:#eee;margin-bottom:8px">Get a modern business presentation that is beautifully designed. Easy to change colors, photos and Text.</li><li style="color:#eee;margin-bottom:8px">Get a modern business presentation that is beautifully designed. Easy to change colors, photos and Text.</li><li style="color:#eee">Get a modern business presentation that is beautifully designed. Easy to change colors, photos and Text.</li></ul>
  <div class="photo" role="img" aria-label="Hand holding a smartphone showing a shopping app" style="left:372px;top:72px;width:144px;height:204px;border-radius:8px;background:linear-gradient(135deg,#e7e7e9,#b5b7bb)"></div>
</section>

<section class="slide">
  <div class="photo" role="img" aria-label="Blurred grey office interior with glass walls" style="inset:0;background:linear-gradient(#d6d6d6,#f2f2f2 40%,#cfcfcf)"></div>
  <div class="abs" style="left:14px;top:14px;width:524px;height:284px;border:2px solid var(--ink)"></div>
  <div class="abs title" style="left:52px;top:66px;font-size:30px">02</div>
  <div class="abs bg-ink" style="left:0;top:104px;width:551px;height:104px"></div>
  <div class="abs title" style="left:52px;top:132px;color:#fff;font-size:17px">SECTION TITLE</div>
  <div class="abs sub" style="left:52px;top:154px;color:#bbb">SUBTITLE GOES HERE</div>
  <div class="abs" style="left:274px;top:122px;width:1px;height:70px;background:var(--yellow)"></div>
  <div class="wordmark" style="left:318px;top:148px;font-size:13px;color:#fff">MEADOWLINE</div>
  <div class="abs" style="left:196px;top:280px;font-size:5px;letter-spacing:3px;font-weight:600">WWW.MEADOWLINE-STUDIO.COM</div>
</section>

<section class="slide">
  <div class="abs title" style="left:32px;top:22px">YOUR TITLE HERE</div>
  <div class="abs sub" style="left:32px;top:44px">SUBTITLE GOES HERE</div>
  <div class="wordmark" style="left:438px;top:30px;font-size:6px">MEADOWLINE</div>
  <svg class="abs" style="left:118px;top:66px" width="200" height="200" viewBox="0 0 200 200">
    <g transform="rotate(-90 100 100)" fill="none" stroke-width="34">
      <circle cx="100" cy="100" r="80" stroke="var(--yellow)" stroke-dasharray="150.8 502.7"/>
      <circle cx="100" cy="100" r="80" stroke="var(--green)" stroke-dasharray="50.3 502.7" stroke-dashoffset="-150.8"/>
      <circle cx="100" cy="100" r="80" stroke="var(--teal)" stroke-dasharray="50.3 502.7" stroke-dashoffset="-201.1"/>
      <circle cx="100" cy="100" r="80" stroke="var(--ink)" stroke-dasharray="251.3 502.7" stroke-dashoffset="-251.4"/>
    </g>
    <text x="100" y="96" text-anchor="middle" font-size="14" font-weight="700" font-family="Montserrat, sans-serif">OUR</text>
    <text x="100" y="113" text-anchor="middle" font-size="14" font-weight="700" font-family="Montserrat, sans-serif">STRUCTURE</text>
    <g fill="#fff" font-size="12" font-family="Montserrat, sans-serif"><text x="160" y="56">30%</text><text x="155" y="148">10%</text><text x="116" y="178">10%</text><text x="4" y="104">50%</text></g>
  </svg>
  <div class="abs" style="left:334px;top:70px;width:1px;height:208px;background:var(--line)"></div>
  <ul class="abs body list bullet" style="left:344px;top:74px;width:180px"><li style="margin-bottom:20px">Get a modern business presentation that is beautifully designed. Easy to change colors, photos and Text.</li><li style="margin-bottom:20px">Get a modern business presentation that is beautifully designed. Easy to change colors, photos and Text.</li><li style="margin-bottom:20px">Get a modern business presentation that is beautifully designed. Easy to change colors, photos and Text.</li><li>Get a modern business presentation that is beautifully designed. Easy to change colors, photos and Text.</li></ul>
  <div class="foot">MEADOWLINE | CLEAR IT FOR GROWTH</div><div class="page">PAGE | 14</div>
  <div class="stripe"><i class="k"></i><i class="t"></i><i class="g"></i><i class="y"></i></div>
</section>

<section class="slide">
  <div class="abs title" style="left:32px;top:22px">YOUR TITLE HERE</div>
  <div class="abs sub" style="left:32px;top:44px">SUBTITLE GOES HERE</div>
  <div class="wordmark" style="left:438px;top:30px;font-size:6px">MEADOWLINE</div>
  <div class="abs bg-ink" style="left:50px;top:90px;width:122px;height:34px;color:#fff;font-size:7px;display:flex;align-items:center;justify-content:center">Sales And Presales</div>
  <div class="abs bg-teal" style="left:50px;top:134px;width:122px;height:34px;color:#fff;font-size:7px;display:flex;align-items:center;justify-content:center">Quintavel</div>
  <div class="abs bg-green" style="left:50px;top:178px;width:122px;height:34px;color:#fff;font-size:7px;display:flex;align-items:center;justify-content:center">Business</div>
  <div class="abs bg-yellow" style="left:50px;top:222px;width:122px;height:34px;color:#222;font-size:7px;display:flex;align-items:center;justify-content:center">Saas Platform</div>
  <div class="abs body" style="left:176px;top:90px;width:350px;height:34px;border:1px solid var(--line);padding:3px 5px">Get a modern business presentation that is beautifully designed. Easy to change colors, photos and Text. You can simply impress your audience and add a unique zing and appeal to your Presentations.</div>
  <div class="abs body" style="left:176px;top:134px;width:350px;height:34px;border:1px solid var(--line);padding:3px 5px">Get a modern business presentation that is beautifully designed. Easy to change colors, photos and Text. You can simply impress your audience and add a unique zing and appeal to your Presentations.</div>
  <div class="abs body" style="left:176px;top:178px;width:350px;height:34px;border:1px solid var(--line);padding:3px 5px">Get a modern business presentation that is beautifully designed. Easy to change colors, photos and Text. You can simply impress your audience and add a unique zing and appeal to your Presentations.</div>
  <div class="abs body" style="left:176px;top:222px;width:350px;height:34px;border:1px solid var(--line);padding:3px 5px">Get a modern business presentation that is beautifully designed. Easy to change colors, photos and Text. You can simply impress your audience and add a unique zing and appeal to your Presentations.</div>
  <div class="foot">MEADOWLINE | CLEAR IT FOR GROWTH</div><div class="page">PAGE | 15</div>
  <div class="stripe"><i class="k"></i><i class="t"></i><i class="g"></i><i class="y"></i></div>
</section>

<section class="slide">
  <div class="abs bg-ink" style="left:0;top:0;width:551px;height:52px"></div>
  <div class="abs title" style="left:32px;top:18px;color:#fff">OUR PARTNERS</div>
  <div class="wordmark" style="left:438px;top:22px;font-size:6px;color:#fff">MEADOWLINE</div>
  <div class="partner" style="left:80px;top:98px"><span class="sq"></span>Quintavel</div>
  <div class="partner" style="left:176px;top:98px">Orbitel</div>
  <div class="partner" style="left:272px;top:98px"><span class="sq"></span>Quintavel</div>
  <div class="partner" style="left:368px;top:98px">Brevon</div>
  <div class="partner" style="left:80px;top:150px">Actavia</div>
  <div class="partner" style="left:176px;top:150px"><span class="sq"></span>Quintavel</div>
  <div class="partner" style="left:272px;top:150px">Lumago</div>
  <div class="partner" style="left:368px;top:150px"><span class="sq"></span>Quintavel</div>
  <div class="partner" style="left:80px;top:202px"><span class="sq"></span>Quintavel</div>
  <div class="partner" style="left:176px;top:202px">Verdano</div>
  <div class="partner" style="left:272px;top:202px"><span class="sq"></span>Quintavel</div>
  <div class="partner" style="left:368px;top:202px;font-size:5px">ADD YOUR LOGO HERE</div>
  <div class="foot">MEADOWLINE | CLEAR IT FOR GROWTH</div><div class="page">PAGE | 16</div>
  <div class="stripe"><i class="k"></i><i class="t"></i><i class="g"></i><i class="y"></i></div>
</section>

<section class="slide">
  <div class="abs title" style="left:32px;top:22px">PRICE TITLE HERE</div>
  <div class="wordmark" style="left:438px;top:30px;font-size:6px">MEADOWLINE</div>
  <div class="abs" style="left:32px;top:48px;width:30px;height:2px;background:linear-gradient(90deg,var(--teal),var(--green),var(--yellow))"></div>
  <div class="price-col" style="left:46px"><div class="head">PACKAGE 1</div><div class="amt" style="background:#6a6a6a">$400</div><p class="body" style="padding:4px">Get a modern business presentation that is beautifully designed.</p><div class="opt">Options Here</div><div class="opt">Options Here</div><div class="opt">Options Here</div><div class="opt">Options Here</div><div class="foot-btn">Ultimate</div></div>
  <div class="price-col" style="left:168px"><div class="head bg-teal">PACKAGE 2</div><div class="amt bg-teal">$200</div><p class="body" style="padding:4px">Get a modern business presentation that is beautifully designed.</p><div class="opt">Options Here</div><div class="opt">Options Here</div><div class="opt">Options Here</div><div class="opt">Options Here</div><div class="foot-btn">Ultimate</div></div>
  <div class="price-col" style="left:290px"><div class="head bg-green">PACKAGE 3</div><div class="amt bg-green">$100</div><p class="body" style="padding:4px">Get a modern business presentation that is beautifully designed.</p><div class="opt">Options Here</div><div class="opt">Options Here</div><div class="opt">Options Here</div><div class="opt">Options Here</div><div class="foot-btn">Ultimate</div></div>
  <div class="price-col" style="left:412px"><div class="head bg-yellow">PACKAGE 4</div><div class="amt bg-yellow" style="color:var(--ink)">$50</div><p class="body" style="padding:4px">Get a modern business presentation that is beautifully designed.</p><div class="opt">Options Here</div><div class="opt">Options Here</div><div class="opt">Options Here</div><div class="opt">Options Here</div><div class="foot-btn">Ultimate</div></div>
  <div class="foot">MEADOWLINE | CLEAR IT FOR GROWTH</div><div class="page">PAGE | 17</div>
  <div class="stripe"><i class="k"></i><i class="t"></i><i class="g"></i><i class="y"></i></div>
</section>

<section class="slide dark">
  <div class="photo" role="img" aria-label="Earth at night seen from space with city lights" style="inset:0;background:radial-gradient(ellipse at 30% 90%,#3a3f52,#0b0d14 60%)"></div>
  <div class="wordmark" style="left:52px;top:50px;font-size:12px;color:#fff">MEADOWLINE</div>
  <div class="abs" style="left:250px;top:56px;font-size:34px;font-weight:700;color:rgba(255,255,255,.18)">01</div>
  <div class="abs title" style="left:34px;top:232px;color:#fff">YOUR TITLE HERE</div>
  <div class="abs sub" style="left:52px;top:254px;color:#bbb">SUBTITLE GOES HERE</div>
  <div class="abs" style="left:394px;top:118px;font-size:6px;font-weight:700;width:128px;text-align:right">TITLE HERE</div>
  <div class="abs body" style="left:294px;top:134px;width:228px;text-align:justify">Get a modern business presentation that is beautifully designed. Easy to change colors, photos and Text. You can simply impress your audience and add a unique zing and appeal to your Presentations. Get a modern business presentation that is beautifully designed. Easy to change colors, photos and Text. You can simply impress your audience and add a unique zing and appeal to your Presentations. Easy to change colors, photos and Text.<br><br>You can simply impress your audience and add a unique zing and appeal to your Presentations.</div>
</section>

<section class="slide">
  <div class="abs title" style="left:32px;top:22px">OUR TEAM</div>
  <div class="abs" style="left:32px;top:48px;width:30px;height:2px;background:linear-gradient(90deg,var(--teal),var(--green),var(--yellow))"></div>
  <div class="wordmark" style="left:438px;top:30px;font-size:6px">MEADOWLINE</div>
  <div class="member" style="left:46px"><div class="pic" role="img" aria-label="Team member portrait photo"></div><div class="name bg-ink">Member Name</div><p class="body" style="margin-top:4px">Get a modern business presentation that is beautifully designed.</p></div>
  <div class="member" style="left:162px"><div class="pic" role="img" aria-label="Team member portrait photo" style="background:linear-gradient(#a23a3a,#d9b8a0)"></div><div class="name bg-teal">Member Name</div><p class="body" style="margin-top:4px">Get a modern business presentation that is beautifully designed.</p></div>
  <div class="member" style="left:278px"><div class="pic" role="img" aria-label="Team member portrait photo" style="background:linear-gradient(#e4e4e4,#6b5544)"></div><div class="name bg-green">Member Name</div><p class="body" style="margin-top:4px">Get a modern business presentation that is beautifully designed.</p></div>
  <div class="member" style="left:394px"><div class="pic" role="img" aria-label="Team member portrait photo" style="background:linear-gradient(#5c5c5c,#2d2622)"></div><div class="name bg-yellow">Member Name</div><p class="body" style="margin-top:4px">Get a modern business presentation that is beautifully designed.</p></div>
  <div class="foot">MEADOWLINE | CLEAR IT FOR GROWTH</div><div class="page">PAGE | 19</div>
  <div class="stripe"><i class="k"></i><i class="t"></i><i class="g"></i><i class="y"></i></div>
</section>

<section class="slide">
  <div class="abs title" style="left:32px;top:22px">YOUR TITLE HERE</div>
  <div class="wordmark" style="left:438px;top:30px;font-size:6px">MEADOWLINE</div>
  <svg class="abs" style="left:0;top:0" width="290" height="309" viewBox="0 0 290 309"><g stroke="#555" stroke-dasharray="2 2" fill="none"><line x1="116" y1="100" x2="138" y2="100"/><path d="M170 116 V132 H96 V152"/><line x1="116" y1="172" x2="138" y2="172"/><path d="M170 188 V204 H96 V224"/></g></svg>
  <div class="step" style="left:58px;top:84px">Step 1</div>
  <div class="step" style="left:140px;top:84px">Step 2</div>
  <div class="step" style="left:58px;top:156px">Step 3</div>
  <div class="step" style="left:140px;top:156px">Step 4</div>
  <div class="step" style="left:58px;top:228px">Step 5</div>
  <div class="abs bg-ink" style="left:288px;top:72px;width:252px;height:196px;border-radius:10px"></div>
  <svg class="abs" style="left:300px;top:84px" width="44" height="176" viewBox="0 0 44 176"><g fill="none" stroke-width="5"><circle cx="22" cy="22" r="16" stroke="#444"/><circle cx="22" cy="22" r="16" stroke="var(--teal)" stroke-dasharray="68.4 100.5" transform="rotate(-90 22 22)"/><circle cx="22" cy="88" r="16" stroke="#444"/><circle cx="22" cy="88" r="16" stroke="var(--green)" stroke-dasharray="35.2 100.5" transform="rotate(-90 22 88)"/><circle cx="22" cy="154" r="16" stroke="#444"/><circle cx="22" cy="154" r="16" stroke="var(--yellow)" stroke-dasharray="55.3 100.5" transform="rotate(-90 22 154)"/></g><g fill="#fff" font-size="8" font-weight="700" text-anchor="middle" font-family="Montserrat, sans-serif"><text x="22" y="25">68%</text><text x="22" y="91">35%</text><text x="22" y="157">55%</text></g></svg>
  <div class="abs" style="left:356px;top:96px;width:170px"><p style="color:var(--teal);font-size:6px;font-weight:600">Contents</p><p class="body">Get a modern business presentation that is beautifully designed.</p></div>
  <div class="abs" style="left:356px;top:162px;width:170px"><p style="color:var(--green);font-size:6px;font-weight:600">Contents</p><p class="body">Get a modern business presentation that is beautifully designed.</p></div>
  <div class="abs" style="left:356px;top:228px;width:170px"><p style="color:var(--yellow);font-size:6px;font-weight:600">Contents</p><p class="body">Get a modern business presentation that is beautifully designed.</p></div>
  <div class="foot">MEADOWLINE | CLEAR IT FOR GROWTH</div><div class="page">PAGE | 20</div>
  <div class="stripe"><i class="k"></i><i class="t"></i><i class="g"></i><i class="y"></i></div>
</section>

<section class="slide">
  <div class="abs" style="left:225px;top:0;width:100px;height:3px;background:linear-gradient(90deg,var(--teal),var(--green),var(--yellow))"></div>
  <div class="abs title" style="left:0;width:551px;text-align:center;top:22px;font-size:18px">FREE EDITABLE ICONS</div>
  <div class="photo" role="img" aria-label="Grid of black line icons for business topics" style="left:24px;top:64px;width:503px;height:226px;background:repeating-linear-gradient(90deg,#fff 0 6px,#e3e3e3 6px 16px);opacity:.8"></div>
  <div class="abs" style="left:225px;bottom:0;width:100px;height:3px;background:linear-gradient(90deg,var(--teal),var(--green),var(--yellow))"></div>
</section>

<section class="slide">
  <div class="abs" style="left:0;top:22px;width:551px;height:60px;background:linear-gradient(90deg,var(--ink) 30%,#fff)"></div>
  <div class="wordmark" style="left:52px;top:44px;font-size:12px;color:#fff">MEADOWLINE</div>
  <div class="photo" role="img" aria-label="Light grey connected network of dots and lines" style="left:300px;top:82px;width:251px;height:215px;background:linear-gradient(135deg,#fff,#ececec)"></div>
  <div class="abs" style="left:34px;top:126px;font-size:9px;font-weight:700">PRESENTER NAME</div>
  <div class="abs" style="left:34px;top:148px;font-size:6.5px;line-height:24px">
    <div><svg width="9" height="9" viewBox="0 0 10 10"><path d="M2 1 L4 1 L5 3 L4 4 Q5 6 6 6 L7 5 L9 6 L9 8 Q5 9 1 3 Z" fill="var(--ink)"/></svg>&nbsp;&nbsp;&nbsp;+1 234 567 890</div>
    <div><svg width="9" height="9" viewBox="0 0 10 10"><circle cx="5" cy="5" r="4" fill="none" stroke="var(--ink)"/><path d="M1 5H9M5 1Q2 5 5 9M5 1Q8 5 5 9" fill="none" stroke="var(--ink)" stroke-width=".7"/></svg>&nbsp;&nbsp;&nbsp;www.yourwebsite.com</div>
    <div><svg width="9" height="9" viewBox="0 0 10 10"><rect x="1" y="2" width="8" height="6" fill="none" stroke="var(--ink)"/><path d="M1 2L5 6L9 2" fill="none" stroke="var(--ink)"/></svg>&nbsp;&nbsp;&nbsp;addyouremail@here.com</div>
    <div><svg width="9" height="9" viewBox="0 0 10 10"><path d="M5 9Q1 5 1 3.8A4 4 0 0 1 9 3.8Q9 5 5 9Z" fill="var(--ink)"/><circle cx="5" cy="3.8" r="1.4" fill="#fff"/></svg>&nbsp;&nbsp;&nbsp;Add your location here</div>
  </div>
  <div class="abs bg-ink" style="left:0;bottom:0;width:420px;height:10px"><span style="color:#fff;font-size:4px;position:absolute;left:16px;top:3px">MEADOWLINE | CLEAR IT FOR GROWTH</span></div>
  <div class="abs bg-teal" style="left:426px;bottom:0;width:38px;height:10px"></div>
  <div class="abs bg-green" style="left:470px;bottom:0;width:38px;height:10px"></div>
  <div class="abs bg-yellow" style="left:513px;bottom:0;width:38px;height:10px"></div>
</section>

</main>
</body>
</html>
```